New Billboard Design Project

I would like to have a banner made which is approx 16ft wide x 8ft tall showing our 3 businesses. I would like to use the new Ridgeline Depot Logo as the main , and have them all incorporated in one banner. I would like to have a nice background that would go with construction, excavation and material supply yard which sells landscape materials,
Updates

Adding photos to be incorporated

Target Market(s)

contractors, homeowners, landscapers, developers

Industry/Entity Type

Construction, land clearing, concrete foundations, Excaavation

Requirements
Must have
• excavation, concrete, all three logos

```html
<!DOCTYPE html>
<html lang="en">
<head>
<meta charset="utf-8">
<title>Ridgeline Depot Billboard</title>
<link rel="stylesheet" href="https://fonts.googleapis.com/css2?family=Playfair+Display:wght@700&family=Montserrat:wght@600;800&display=swap">
<style>
  :root {
    --stage: #b4b4b4;
    --paper: #ffffff;
    --dot-light: #f7f7f7;
    --dot-tone: #d9d9d9;
    --maroon: #6e1a22;
    --red: #d7212b;
    --red-light: #e8404a;
    --red-deep: #a3111a;
    --silver-light: #f4f4f4;
    --silver-dark: #7d7d7d;
    --ink: #3a3a3a;
  }
  html, body {
    margin: 0;
    padding: 0;
    width: 789px;
    height: 1200px;
    overflow: hidden;
    background: var(--stage);
  }
  .billboard {
    position: absolute;
    left: 30px;
    top: 420px;
    width: 729px;
    height: 353px;
    box-shadow: 6px 8px 12px rgba(0,0,0,0.45);
  }
  .billboard svg { display: block; width: 100%; height: 100%; }
  .brand-name { font-family: "Playfair Display", Georgia, serif; font-weight: 700; fill: var(--maroon); }
  .partner-name { font-family: "Montserrat", Arial, sans-serif; font-weight: 800; fill: var(--ink); }
  .partner-phone { font-family: "Montserrat", Arial, sans-serif; font-weight: 600; fill: var(--red); }
</style>
</head>
<body>
<div class="billboard">
  <svg viewBox="0 0 930 450" xmlns="http://www.w3.org/2000/svg">
    <defs>
      <linearGradient id="frame-silver" x1="0" y1="0" x2="1" y2="1">
        <stop offset="0" stop-color="var(--silver-light)"/>
        <stop offset="0.5" stop-color="var(--silver-dark)"/>
        <stop offset="1" stop-color="var(--silver-light)"/>
      </linearGradient>
      <radialGradient id="halftone-field" cx="0.5" cy="0.3" r="0.75">
        <stop offset="0" stop-color="var(--paper)"/>
        <stop offset="0.45" stop-color="var(--dot-light)"/>
        <stop offset="1" stop-color="var(--dot-tone)"/>
      </radialGradient>
      <linearGradient id="red-band" x1="0" y1="0" x2="1" y2="1">
        <stop offset="0" stop-color="var(--red)"/>
        <stop offset="0.5" stop-color="var(--red-light)"/>
        <stop offset="1" stop-color="var(--red-deep)"/>
      </linearGradient>
      <linearGradient id="line-texture" x1="0" y1="0" x2="1" y2="0">
        <stop offset="0" stop-color="var(--red-deep)" stop-opacity="0.7"/>
        <stop offset="0.5" stop-color="var(--red-light)" stop-opacity="0.35"/>
        <stop offset="1" stop-color="var(--red-deep)" stop-opacity="0.75"/>
      </linearGradient>
      <linearGradient id="ring-silver" x1="0" y1="0" x2="1" y2="1">
        <stop offset="0" stop-color="#ffffff"/>
        <stop offset="0.45" stop-color="#6f6f6f"/>
        <stop offset="1" stop-color="#e8e8e8"/>
      </linearGradient>
    </defs>

    <rect class="halftone-field" x="0" y="0" width="930" height="450" fill="url(#halftone-field)" role="img" aria-label="Soft grey halftone dot pattern"/>

    <path class="red-wave" d="M0,236 C220,228 480,268 660,258 C780,250 870,228 930,214 L930,450 L0,450 Z" fill="url(#red-band)"/>
    <path class="line-texture" d="M0,300 C260,270 560,350 930,280 L930,450 L0,450 Z" fill="url(#line-texture)" role="img" aria-label="Fine wavy line texture across the red band"/>
    <path class="wave-edge" d="M0,236 C220,228 480,268 660,258 C780,250 870,228 930,214" fill="none" stroke="var(--paper)" stroke-width="3" opacity="0.85"/>

    <text class="brand-name" x="465" y="128" text-anchor="middle" font-size="56">Ridgeline Depot</text>

    <g class="partner partner-excavation">
      <circle cx="170" cy="274" r="116" fill="url(#ring-silver)"/>
      <circle cx="170" cy="274" r="106" fill="var(--paper)"/>
      <text class="partner-name" x="170" y="270" text-anchor="middle" font-size="22">Stonebrook</text>
      <text class="partner-name" x="170" y="298" text-anchor="middle" font-size="13" letter-spacing="1.5">EXCAVATION CO.</text>
    </g>

    <g class="partner partner-truck">
      <circle cx="455" cy="312" r="116" fill="url(#ring-silver)"/>
      <circle cx="455" cy="312" r="106" fill="var(--paper)"/>
      <text class="partner-name" x="455" y="304" text-anchor="middle" font-size="26">Ironway</text>
      <text class="partner-name" x="455" y="330" text-anchor="middle" font-size="15">TRUCK REPAIR</text>
      <text class="partner-phone" x="455" y="354" text-anchor="middle" font-size="13" letter-spacing="1">(555) 014-2290</text>
    </g>

    <g class="partner partner-homes">
      <circle cx="740" cy="272" r="118" fill="url(#ring-silver)"/>
      <circle cx="740" cy="272" r="107" fill="var(--paper)"/>
      <text class="partner-name" x="740" y="266" text-anchor="middle" font-size="24">Maplecrest</text>
      <text class="partner-name" x="740" y="290" text-anchor="middle" font-size="15">HOMES</text>
      <text class="partner-name" x="740" y="310" text-anchor="middle" font-size="9" letter-spacing="1">CONSTRUCTION CO.</text>
    </g>

    <rect class="frame" x="3" y="3" width="924" height="444" fill="none" stroke="url(#frame-silver)" stroke-width="6"/>
  </svg>
</div>
</body>
</html>
```